Larkfield Claim Services Philosophy/Positioning Flyer

I want to create a one page promotional ad/flyer to describe a little about our viewpoint.
The idea is we focus on fundamentals, which are often viewed as the small steps. But we recognize today’s challenges, but hold value in what the adjusting process and the adjuster deliver; recognizing it impacts both a consumer concern and a carrier concern. It’s a small thing but we do it in a great way. We just want to be the best.

Target Market(s)

Insurance company vendor managers and claims personnel

Industry/Entity Type

Insurance

Requirements
Must have
• professional, clean design, good flow, something that sells quality
Nice to have
• good color blend
Should not have
• cartoon type graphics or photos

```html
<!DOCTYPE html>
<html lang="en">
<head>
<meta charset="utf-8">
<title>Larkfield Claim Services – Focus on the Fundamentals</title>
<link href="https://fonts.googleapis.com/css2?family=Source+Sans+3:wght@400;600;700&display=swap" rel="stylesheet">
<style>
  :root{
    --page:#dcdde0;
    --paper:#f1f2f4;
    --blue-deep:#0a5ca8;
    --blue-mid:#1a86cf;
    --blue-bright:#2fa4de;
    --band:#8ed8f8;
    --ink:#3a3a3a;
    --ink-soft:#4a4a4a;
    --white:#ffffff;
  }
  *{box-sizing:border-box;margin:0;padding:0}
  html,body{width:1200px;height:1200px;overflow:hidden}
  body{background:var(--page);font-family:"Source Sans 3",Arial,sans-serif;color:var(--ink)}
  .flyer{position:absolute;left:176px;top:0;width:848px;height:1200px;background:var(--paper);overflow:hidden}

  /* header */
  .header{position:absolute;left:0;top:0;width:100%;height:231px}
  .brand{position:absolute;left:39px;top:78px;width:350px;display:flex;align-items:center;gap:14px}
  .brand-square{width:34px;height:34px;background:var(--blue-mid);flex:none}
  .brand-name{font-size:30px;font-weight:700;color:var(--blue-deep);line-height:1.05}
  .fundamentals{position:absolute;left:424px;top:28px;width:400px}
  .fundamentals-title{border-left:5px solid #5b5b5b;padding-left:12px;color:var(--blue-mid);line-height:1.25;font-size:22px;font-weight:600}
  .fundamentals-title strong{display:block;color:var(--blue-deep);font-weight:700;font-size:24px}
  .checklist{list-style:none;margin-top:10px;padding-left:16px}
  .checklist li{display:flex;align-items:center;gap:9px;font-size:13.6px;color:var(--ink-soft);height:24.4px}
  .checklist svg{flex:none}

  /* headline band */
  .headline-band{position:absolute;left:0;top:231px;width:100%;height:121px;background:var(--band)}
  .headline{position:absolute;left:39px;top:14px;width:790px;font-size:34.5px;font-weight:700;line-height:1.18;color:var(--ink)}

  /* photo */
  .photo{position:absolute;left:0;top:352px;width:100%;height:379px;
    background:linear-gradient(115deg,#8a8f96 0%,#c9ccd0 28%,#e6eef5 48%,#9fc6e8 62%,#f4f6f8 80%,#d9dadb 100%)}
  .photo-tag{position:absolute;right:0;top:0;width:368px;height:87px;background:rgba(22,130,205,.82);
    clip-path:polygon(0 0,100% 0,100% 100%,18% 100%);
    color:var(--white);font-size:31px;font-weight:600;line-height:1.17;text-align:right;padding:5px 40px 0 0}

  /* bottom */
  .bottom{position:absolute;left:0;top:731px;width:100%;height:469px}
  .bottom-strip{position:absolute;left:0;top:0;width:100%;height:14px;background:var(--band)}
  .story{position:absolute;left:39px;top:28px;width:408px}
  .story-lead{color:var(--blue-deep);font-size:19.5px;line-height:1.23;text-align:justify;font-weight:600}
  .story-lead b{font-weight:700}
  .story-lead + .story-lead{margin-top:8px}
  .story p{font-size:15.8px;line-height:1.3;text-align:justify;color:#2a2a2a;margin-top:10px}
  .story p + p{margin-top:12px}
  .tagline{color:var(--blue-mid);font-weight:700;font-size:16px;line-height:1.3;margin:6px 0 0 57px}

  .contact-panel{position:absolute;left:467px;top:14px;width:381px;height:455px;
    background:linear-gradient(160deg,#1f7fc8 0%,#2ea1dc 45%,#1b7cc4 100%);
    clip-path:polygon(0 0,100% 0,100% 100%,0 100%,0 196px,44px 146px,0 96px)}
  .award-placeholder{position:absolute;left:118px;top:48px;width:150px;height:150px;border-radius:50%;
    background:rgba(255,255,255,.22)}
  .recommend{position:absolute;left:22px;top:247px;width:350px;color:var(--white);font-size:20px;font-weight:600;white-space:nowrap}
  .contacts{position:absolute;left:14px;top:300px;list-style:none}
  .contacts li{display:flex;align-items:flex-start;gap:16px;color:var(--white);font-weight:700;font-size:18.5px;line-height:1.25;margin-bottom:12px}
  .contacts svg{flex:none;margin-top:1px}
</style>
</head>
<body>
<main class="flyer">
  <header class="header">
    <div class="brand">
      <span class="brand-square"></span>
      <span class="brand-name">Larkfield Claim Services</span>
    </div>
    <section class="fundamentals">
      <h2 class="fundamentals-title">At Larkfield Claim Services, we <strong>Focus on the Fundamentals</strong></h2>
      <ul class="checklist">
        <li><svg width="11" height="10" viewBox="0 0 11 10"><rect x="0.5" y="1.5" width="8" height="8" fill="none" stroke="#1a86cf"/><path d="M2 5l2.2 2.2L10 1" fill="none" stroke="#0a5ca8" stroke-width="1.6"/></svg>Immediate contact with the policyholder</li>
        <li><svg width="11" height="10" viewBox="0 0 11 10"><rect x="0.5" y="1.5" width="8" height="8" fill="none" stroke="#1a86cf"/><path d="M2 5l2.2 2.2L10 1" fill="none" stroke="#0a5ca8" stroke-width="1.6"/></svg>Prompt scoping of the loss</li>
        <li><svg width="11" height="10" viewBox="0 0 11 10"><rect x="0.5" y="1.5" width="8" height="8" fill="none" stroke="#1a86cf"/><path d="M2 5l2.2 2.2L10 1" fill="none" stroke="#0a5ca8" stroke-width="1.6"/></svg>Expedient submission of an accurate estimate to the carrier</li>
        <li><svg width="11" height="10" viewBox="0 0 11 10"><rect x="0.5" y="1.5" width="8" height="8" fill="none" stroke="#1a86cf"/><path d="M2 5l2.2 2.2L10 1" fill="none" stroke="#0a5ca8" stroke-width="1.6"/></svg>Responsive communication</li>
        <li><svg width="11" height="10" viewBox="0 0 11 10"><rect x="0.5" y="1.5" width="8" height="8" fill="none" stroke="#1a86cf"/><path d="M2 5l2.2 2.2L10 1" fill="none" stroke="#0a5ca8" stroke-width="1.6"/></svg>Thorough file documentation</li>
      </ul>
    </section>
  </header>

  <section class="headline-band">
    <h1 class="headline">They may seem small, but the ripple effect of doing the basic things right is extraordinary.</h1>
  </section>

  <section class="photo" role="img" aria-label="Photo of hands pointing at charts on a tablet beside a cup of coffee on a desk">
    <div class="photo-tag">Small things done in<br>a great way!</div>
  </section>

  <section class="bottom">
    <div class="bottom-strip"></div>
    <article class="story">
      <h3 class="story-lead"><b>The challenge today:</b> Meet the consumers’ ever-changing expectations and demands driven by advances in technology.</h3>
      <h3 class="story-lead">But is new technology the answer? Is claim estimating a self-service insurance item?</h3>
      <p>While technology may produce some cost savings and improve the estimating process, the fundamental process of an adjuster meeting with the policyholder and doing a physical inspection is still the most reliable method for preparing an accurate estimate. And, accurate indemnification supports policyholder retention through rate stability… which is also a consumer concern.</p>
      <p>Besides, a smile, a handshake and doing business face to face will deliver a positive experience during a troubled time.</p>
      <div class="tagline">We may not be the only IA firm you use,<br>we just want to be the best one you use.</div>
    </article>

    <aside class="contact-panel" role="img" aria-label="Blue-toned photo of office towers behind the contact details">
      <div class="award-placeholder" role="img" aria-label="Industry recognition badge"></div>
      <div class="recommend">Proud to be recommended by Crestline</div>
      <ul class="contacts">
        <li><svg width="22" height="28" viewBox="0 0 22 28"><path d="M11 1C5.5 1 1.5 5 1.5 10.3 1.5 17 11 27 11 27s9.5-10 9.5-16.7C20.5 5 16.5 1 11 1z" fill="#fff"/><circle cx="11" cy="10.5" r="3.8" fill="#2a93d5"/></svg><span>418 Harbor Lane #210, Fairmont Ridge,<br>CA. 93990</span></li>
        <li><svg width="24" height="24" viewBox="0 0 24 24"><path d="M6 2l4 5-2.5 2.5c1.2 2.8 3.8 5.4 6.5 6.5L16.5 13.5l5 4-2.5 4c-8.5 0-17-8.5-17-17z" fill="none" stroke="#fff" stroke-width="2" stroke-linejoin="round"/><path d="M14 2a8 8 0 0 1 8 8M14 6a4 4 0 0 1 4 4" fill="none" stroke="#fff" stroke-width="1.8"/></svg><span>(555) 214-3080</span></li>
        <li><svg width="24" height="28" viewBox="0 0 24 28"><rect x="1" y="8" width="6" height="19" rx="1" fill="none" stroke="#fff" stroke-width="2"/><rect x="9" y="2" width="14" height="25" rx="1" fill="none" stroke="#fff" stroke-width="2"/><rect x="12" y="6" width="8" height="5" fill="#fff"/><g fill="#fff"><rect x="12" y="14" width="2.5" height="2.5"/><rect x="16" y="14" width="2.5" height="2.5"/><rect x="12" y="18" width="2.5" height="2.5"/><rect x="16" y="18" width="2.5" height="2.5"/><rect x="12" y="22" width="2.5" height="2.5"/><rect x="16" y="22" width="2.5" height="2.5"/></g></svg><span>(555) 214-3091</span></li>
      </ul>
    </aside>
  </section>
</main>
</body>
</html>
```